Etiketten-Design für Imkerei
Zielgruppe
Wir sind eine kleine Imkerei die sich vorwiegend auf Honig konzentriert. Waldhonig und Wald-Blütenhonig .
Zielgruppe sind alle die gerne Qualitätshonig aus der Region kaufen .
Aufgabenstellung
es sind 2 verschiedene Etiketten Größen für verschieden Nettofüllmengen :
250 g - H 3,5 cm ,B 12 cm
500 g - H 5 cm , B 17 cm
Honigsortenbezeichnung je einmal 'Wald' einmal 'Wald-Blüten' sollte aber möglich sein auch andere Honigsorten anzugeben.
die gesetzlichen Vorschriften der Schriftgröße für Adresse, Haltbarkeit und 100% Honig aus Österreich sind 1,2 mm immer vom kleinsten Buchstaben ausgehend . Ausgenommen NETTOFÜLLMENGE muss mind. 4 mm sein auch vom kleinsten Buchstaben ausgehend .
die Adresse und Mindestens Haltbar bis auf der linken Seite der Etikette( muss auf der gleichen Seite stehen) , in der Mitte Schriftzug mit Grafik wobei hier die Größe keiner Vorschrift unterliegt.
Sortenbezeichnung kann in der Mitte sein muss aber nicht und rechts neben Schriftzug „KOLMER`S HONIG“ die Nettofüllmenge , ganz rechts dann 100% Honig aus Österreich
Die Hintergrundfarbe der Etiketten sollten in Granitgrau- Schwarz lebendig also ähnlich wie marmoriert sein.
Schriftzug in der Mitte : ' Kolmer`s Honig ' das 'B' sollte eine Biene sein , den Rest überlasse ich Euch Profis . Schriftfarbe nicht Metallic oder Gold da die Deckel Silber sind. Fotos füge ich unten ein wobei es weder diese Biene sein muss noch der Schriftzug das ist nur ein Beispiel. Das ganze sollte edel und doch verspielt aussehen . Den Schriftzug Kolmer`s Honig möchte ich in weiterer Folge auch alleine verwenden können wie zB. für Rechnungen oder Homepage .
Angaben auf der Etikette wie oben beschrieben:
Imkerei
T & L Wimmerhuber
Tannenhoferweg 214
9560 Lindenau
+436608274316 1,2 mm ausgehend vom kleinsten Buchstaben
Mindestens Haltbar bis:
siehe Glasunterseite
Trocken und vor Wärme geschützt Lagern ! 1,2 mm ausgehend vom kleinsten Buchstaben

```html
<!DOCTYPE html>
<html lang="de">
<head>
<meta charset="utf-8">
<title>Kolmer`s Honig – Etikette 500 g</title>
<link href="https://fonts.googleapis.com/css2?family=Oswald:wght@300;400&family=Open+Sans:wght@400&family=Cinzel:wght@400&display=swap" rel="stylesheet">
<style>
  :root {
    --page: #ffffff;
    --granite-dark: #1e1e1e;
    --granite-mid: #2c2c2b;
    --granite-light: #3a3a38;
    --text-muted: #8f8a7e;
    --text-light: #a8a395;
    --honey-green: #8a9a12;
    --ring: #6f685c;
  }
  * { margin: 0; padding: 0; box-sizing: border-box; }
  html, body {
    width: 1200px; height: 848px; overflow: hidden;
    background: var(--page);
  }
  .label {
    position: absolute;
    left: 20px; top: 253px;
    width: 1160px; height: 342px;
    overflow: hidden;
    background:
      radial-gradient(ellipse 40% 60% at 20% 30%, var(--granite-light) 0%, transparent 70%),
      radial-gradient(ellipse 35% 50% at 75% 20%, var(--granite-mid) 0%, transparent 70%),
      radial-gradient(ellipse 50% 70% at 55% 80%, #333331 0%, transparent 70%),
      linear-gradient(100deg, var(--granite-mid), var(--granite-dark) 45%, var(--granite-mid) 70%, var(--granite-dark));
  }
  .flora-band {
    position: absolute; left: 0; right: 0; bottom: 0; height: 170px;
    background: linear-gradient(180deg, transparent 0%, rgba(74,70,61,0.35) 45%, rgba(74,70,61,0.55) 100%);
  }
  .producer-info {
    position: absolute; left: 29px; top: 26px;
    font-family: "Oswald", sans-serif; font-weight: 300;
    font-size: 18px; line-height: 24px;
    color: var(--text-muted);
    letter-spacing: -0.2px;
  }
  .producer-info p + p { margin-top: 8px; }
  .brand-ring {
    position: absolute; left: 0; top: 0;
  }
  .brand-name {
    position: absolute; left: 396px; top: 24px; width: 360px;
    display: flex; align-items: center; justify-content: center; gap: 12px;
    font-family: "Oswald", sans-serif; font-weight: 400;
    font-size: 42px; line-height: 1;
    color: var(--honey-green);
  }
  .brand-dot {
    width: 20px; height: 20px; border-radius: 50%;
    background: var(--honey-green); flex: none;
  }
  .variety {
    position: absolute; left: 416px; top: 200px; width: 320px;
    text-align: center;
    font-family: "Cinzel", serif; font-weight: 400;
    font-size: 26px; line-height: 34px;
    color: var(--honey-green);
  }
  .variety .big { font-size: 33px; }
  .origin {
    position: absolute; right: 15px; top: 13px;
    font-family: "Open Sans", sans-serif; font-size: 20px; line-height: 28px;
    color: var(--honey-green);
  }
  .net-quantity {
    position: absolute; left: 1033px; top: 54px;
    font-family: "Open Sans", sans-serif;
    color: var(--text-light);
  }
  .net-quantity .caption { font-size: 22px; line-height: 32px; }
  .net-quantity .amount { font-size: 26px; line-height: 36px; }
</style>
</head>
<body>
  <section class="label">
    <div class="flora-band" role="img" aria-label="Dezentes Blüten- und Blätterornament im unteren Bereich der Etikette"></div>

    <div class="producer-info">
      <p>Imkerei<br>T &amp; L Wimmerhuber<br>Tannenhoferweg 214<br>9560 Lindenau</p>
      <p>Mindestens Haltbar bis:<br>siehe Glasunterseite</p>
      <p>Trocken und vor Wärme geschützt<br>Lagern !</p>
    </div>

    <svg class="brand-ring" width="1160" height="342" viewBox="0 0 1160 342" aria-hidden="true">
      <circle cx="575" cy="208" r="124" fill="none" stroke="var(--ring)" stroke-width="3"/>
    </svg>

    <div class="brand-name"><span class="brand-dot"></span>Kolmer`s Honig</div>

    <div class="variety">
      <span class="big">W</span>ald-<span class="big">B</span>lüten-<br><span class="big">H</span>onig
    </div>

    <div class="origin">Honig aus Österreich</div>

    <div class="net-quantity">
      <div class="caption">Füllmenge</div>
      <div class="amount">500g</div>
    </div>
  </section>
</body>
</html>
```